Relaunch Instagram Posts Design

We want to give you a better understanding about the expected outcome of this task, and give you a little bit of a background that should help you throughout.
We already have social media accounts, they aren’t active and the posts are outdated. We just finished our rebranding exercise, and accordingly we are planning to have a re-launch where we communicate our new identity, and rebuild our online existence, to enhance our social media presence and engagement.
Thus, we want to formulate the style of posting from the beginning, so that it reflects the identity overall and we can move forward with in a consistent manner.

Find attached details. We will share other files later. You need to read the attachment in the project to understand the requirement. Also, you should use the attached images in the project. You should also use products images from our website...www.bloomvantra.com
Our Primary color is #5725A9, PURPLE (based on color HEX Code)
Our Secondary colors #7C50BE, #A17BD3, #C5A6E8, #EAD1FD
Also, this secondary colors can be used #2B9348, #55A630, #80B918, #AACC00

Target Market(s)

Gift-givers who would like to bring a gift of value and meaning, representing the occasion

Industry/Entity Type

Flowers

Colors

Designer to choose colors to be used in the design.

Requirements
Must have
• Image based posts with little graphics + typography-based posts.... hammer on the emotional aspect, focusing on special moments such as using images related nice moments
Nice to have
• A full overview as in the brief (with all 21 posts), to give the sense of the design direction for us to know if it fits our new brand vision or not.
Should not have
• A typical commercial design direction that focuses so much on direct product communication. This definitely will be there, but we want this to be integrated with the other aspects.

```html
<!DOCTYPE html>
<html lang="en">
<head>
<meta charset="utf-8">
<title>Bloomvantra – Relaunch Posts</title>
<link rel="stylesheet" href="https://fonts.googleapis.com/css2?family=Montserrat:wght@400;500;600;700&family=Cinzel:wght@500&family=Great+Vibes&display=swap">
<style>
  :root {
    --purple: #5725A9;
    --purple-deep: #4a1c93;
    --purple-mid: #7C50BE;
    --lilac: #A17BD3;
    --lilac-soft: #C5A6E8;
    --lilac-pale: #EAD1FD;
    --mist: #f1e9f8;
    --canvas: #ececec;
    --white: #ffffff;
    --gold: #e0b04a;
    --ink: #6f5a8a;
  }
  * { box-sizing: border-box; margin: 0; padding: 0; }
  html, body { width: 1200px; height: 2400px; overflow: hidden; }
  body {
    background: var(--canvas);
    font-family: "Montserrat", sans-serif;
    position: relative;
  }

  /* ---------- Memory post ---------- */
  .memory-post {
    position: absolute; left: 200px; top: 370px;
    width: 800px; height: 800px;
    display: flex; overflow: hidden;
    box-shadow: 0 10px 30px rgba(0,0,0,.15);
  }
  .memory-post__photo {
    width: 400px; height: 100%;
    background: linear-gradient(160deg, #bdbdbd 0%, #7d7d7d 45%, #3f3f3f 100%);
  }
  .memory-post__panel {
    width: 400px; height: 100%;
    background: radial-gradient(circle at 60% 40%, var(--purple-mid) 0%, var(--purple) 55%, var(--purple-deep) 100%);
    color: var(--white);
    display: flex; flex-direction: column; align-items: center;
    padding: 70px 40px 0 90px;
    text-align: center;
  }
  .memory-post__products {
    position: absolute; left: 270px; top: 200px;
    display: flex; flex-direction: column; gap: 40px;
  }
  .product-bubble {
    width: 130px; height: 130px; border-radius: 50%;
    border: 5px solid var(--white);
    background: radial-gradient(circle at 45% 45%, #a3342e 0%, #5c1a18 60%, #f3ece6 61%, #e7ddd2 100%);
  }
  .product-bubble--cream { background: radial-gradient(circle at 50% 50%, #c9a37b 0%, #8c6744 55%, #f4efe8 56%, #e8e0d6 100%); }
  .product-bubble--dark { background: radial-gradient(circle at 50% 50%, #3d6b34 0%, #1f2e1a 55%, #f2ede6 56%, #e5dcd2 100%); }
  .brand-lockup {
    display: flex; align-items: center; gap: 10px;
    font-weight: 600; font-size: 34px; letter-spacing: .5px;
  }
  .brand-lockup__dot { width: 14px; height: 14px; border-radius: 50%; background: var(--gold); }
  .memory-post__message {
    margin-top: 110px;
    font-size: 30px; line-height: 1.3; font-weight: 500;
  }

  /* ---------- Feed overview grid ---------- */
  .feed-grid {
    position: absolute; left: 50px; top: 1310px;
    width: 1100px; height: 720px;
    display: grid;
    grid-template-columns: repeat(3, 1fr);
    grid-template-rows: repeat(2, 1fr);
    box-shadow: 0 10px 30px rgba(0,0,0,.12);
  }
  .tile { position: relative; overflow: hidden; min-width: 0; }
  .tile--soft { background: linear-gradient(135deg, var(--mist) 0%, var(--lilac-pale) 100%); }
  .tile--white { background: var(--white); }
  .tile--purple {
    background: radial-gradient(circle at 50% 45%, var(--purple-mid) 0%, var(--purple) 60%, var(--purple-deep) 100%);
    color: var(--white); text-align: center;
  }
  .tile__stack { height: 100%; display: flex; flex-direction: column; }
  .tile__stack > .category { flex: 1; }
  .category {
    display: flex; flex-direction: column; align-items: center; justify-content: center;
    gap: 12px; color: var(--ink); font-size: 22px; font-weight: 500; text-align: center; line-height: 1.2;
  }
  .category svg { width: 52px; height: 52px; stroke: var(--lilac); fill: none; stroke-width: 2; }
  .category--alt { background: rgba(255,255,255,.55); }
  .category--gifts { height: 100%; justify-content: flex-start; padding-top: 80px; }
  .bouquet-corner {
    position: absolute; left: 0; bottom: 0; width: 200px; height: 150px;
    border-top-right-radius: 100px;
    background: linear-gradient(45deg, #d9487f 0%, #f29ab9 55%, #9ccf7a 100%);
  }
  .brand-tile {
    display: flex; flex-direction: column; align-items: center; justify-content: center;
    height: 100%; gap: 18px; padding: 0 24px;
  }
  .brand-tile .brand-lockup { color: var(--purple); font-size: 42px; }
  .brand-tile .brand-lockup__dot { width: 18px; height: 18px; background: var(--purple-mid); }
  .hashtag {
    font-family: "Great Vibes", cursive; color: var(--purple-mid);
    font-size: 29px; white-space: nowrap; text-align: center;
  }
  .slogan { height: 100%; display: flex; flex-direction: column; justify-content: center; align-items: center; }
  .slogan__lead { font-family: "Cinzel", serif; font-size: 50px; letter-spacing: 6px; color: var(--lilac-pale); }
  .slogan__script { font-family: "Great Vibes", cursive; font-size: 58px; color: var(--gold); line-height: 1.05; }
  .slogan__tail { font-family: "Cinzel", serif; font-size: 44px; letter-spacing: 4px; color: var(--lilac-pale); }
  .since-tile {
    background: radial-gradient(circle at 40% 60%, #e04f8c 0%, #f4a6c6 45%, #f6e1ea 100%);
  }
  .since-tile__label {
    position: absolute; right: 30px; top: 40px; text-align: right; color: var(--white);
  }
  .since-tile__label small { display: block; font-family: "Great Vibes", cursive; font-size: 40px; }
  .since-tile__label strong { font-size: 110px; font-weight: 700; line-height: .9; }
</style>
</head>
<body>

<section class="memory-post">
  <div class="memory-post__photo" role="img" aria-label="Black and white photo of a living room with an armchair"></div>
  <div class="memory-post__products">
    <div class="product-bubble" role="img" aria-label="Preserved red roses in a gift box"></div>
    <div class="product-bubble product-bubble--cream" role="img" aria-label="Preserved roses in a cream vase"></div>
    <div class="product-bubble product-bubble--dark" role="img" aria-label="Preserved flower arrangement in a dark pot"></div>
  </div>
  <div class="memory-post__panel">
    <div class="brand-lockup"><span class="brand-lockup__dot"></span>Bloomvantra</div>
    <p class="memory-post__message">Our Hearts stay connects to memories. No matter where life takes us, we don't let go of the special moments and people shared with.</p>
  </div>
</section>

<section class="feed-grid">
  <div class="tile tile--soft">
    <div class="tile__stack">
      <div class="category">
        <svg viewBox="0 0 52 52"><circle cx="26" cy="20" r="10"/><path d="M26 30v16M26 40c-6 0-10-4-10-8M26 40c6 0 10-4 10-8"/></svg>
        Preserved<br>Flowers
      </div>
      <div class="category category--alt">
        <svg viewBox="0 0 52 52"><path d="M18 14c4-6 12-6 16 0c4 6-2 14-8 16c-6-2-12-10-8-16z"/><path d="M26 30v16"/></svg>
        Roses
      </div>
    </div>
  </div>

  <div class="tile tile--white">
    <div class="brand-tile">
      <div class="brand-lockup"><span class="brand-lockup__dot"></span>Bloomvantra</div>
      <div class="hashtag">#MomentsFrozenInTime</div>
    </div>
  </div>

  <div class="tile tile--soft">
    <div class="tile__stack">
      <div class="category">
        <svg viewBox="0 0 52 52"><rect x="10" y="20" width="32" height="24"/><path d="M8 20h36M26 20v24M26 20c-4-8-12-8-10-2M26 20c4-8 12-8 10-2"/></svg>
        Occassions
      </div>
      <div class="category category--alt">
        <svg viewBox="0 0 52 52"><path d="M26 44C10 32 8 24 12 18c4-6 12-4 14 2c2-6 10-8 14-2c4 6 2 14-14 26z"/></svg>
        Passion<br>Projects
      </div>
    </div>
  </div>

  <div class="tile tile--soft">
    <div class="category category--gifts">
      <svg viewBox="0 0 52 52"><rect x="10" y="20" width="32" height="24"/><path d="M8 20h36M26 20v24"/></svg>
      Gifts for Every<br>Occassions
    </div>
    <div class="bouquet-corner" role="img" aria-label="Pink tulips bouquet"></div>
  </div>

  <div class="tile tile--purple">
    <div class="slogan">
      <div class="slogan__lead">HELPING</div>
      <div class="slogan__script">Nature's Beauty</div>
      <div class="slogan__tail">Last Forever</div>
    </div>
  </div>

  <div class="tile since-tile" role="img" aria-label="Bouquet of pink and white roses">
    <div class="since-tile__label"><small>Since</small><strong>2005</strong></div>
  </div>
</section>

</body>
</html>
```